Business card for hi tech component manufacturer, specialising in after market firearms components a
Tovin Industries (Ti)
Use same font as used in my logo
Owen Petrie
General Manager
Postal: PO Box 58491, Brackley, Christchurch 8245, New Zealand
Physical: 14 Garnet Street, Fenwick, Christchurch 8024, New Zealand
sales@tovin-works.example.nz
tovin-works.example.nz
Details are to be confirmed in future. Please allow space for Addresses, Phone, Cell, Email and Web address.
Hi Quill42,
You are the winner of the stationary project for Tovin Industries.
We have had some commercial issues with the company name Tovin, and as this is a start up company, we have changed the name.
The new Company name is ZENTH Industries. I have the new logo file, how do I send this to you?
As such I have a new set of address and company name for you to change for the final design.
And the only contact details we want on all the stationary options that you supplied are as follows:
Web: www.zenth.example.nz
Email address: sales@zenth.example.nz
Phone: +6429184306
Contact: Owen Petrie General Manager
Please advise, if you require a different file type, I have .ai, .eps, .gif, .pdf, .png, .psd, .jpg, .tif
I look forward to hearing from you.
Best regards,
Owen

```html
<!DOCTYPE html>
<html lang="en">
<head>
<meta charset="utf-8">
<title>ZENTH Industries — Stationery Set</title>
<link rel="stylesheet" href="https://fonts.googleapis.com/css2?family=Michroma&display=swap">
<style>
  :root {
    --backdrop: #ececec;
    --paper: #ffffff;
    --brand: #3b5670;
    --ink: #4a5561;
    --muted: #8b949c;
    --faint: #eef1f3;
    --edge: #dcdcdc;
    --flap-text: #c7d2dc;
  }
  * { margin: 0; padding: 0; box-sizing: border-box; }
  html, body { width: 1200px; height: 936px; overflow: hidden; }
  body {
    background: var(--backdrop);
    font-family: "Michroma", "Helvetica Neue", Arial, sans-serif;
    color: var(--ink);
    position: relative;
  }
  .sheet {
    position: absolute;
    background: var(--paper);
    border: 1px solid var(--edge);
  }
  .wordmark {
    display: flex;
    align-items: center;
    color: var(--brand);
    letter-spacing: 0.06em;
    white-space: nowrap;
  }
  .wordmark .mark { background: var(--brand); flex: none; }

  /* Letterhead */
  .letterhead { left: 168px; top: 66px; width: 405px; height: 553px; }
  .letterhead .wordmark { position: absolute; left: 20px; top: 22px; font-size: 8px; gap: 6px; }
  .letterhead .wordmark .mark { width: 22px; height: 22px; }
  .letterhead .contact {
    position: absolute; left: 262px; top: 20px;
    font-size: 4.5px; line-height: 9px; color: var(--muted); list-style: none;
    white-space: nowrap;
  }
  .letterhead .contact li { display: flex; align-items: center; gap: 4px; }
  .letterhead .contact li::before {
    content: ""; width: 4px; height: 4px; background: var(--brand); border-radius: 50%;
  }
  .letterhead .watermark {
    position: absolute; left: 128px; top: 190px; width: 150px; height: 150px;
    background: var(--faint);
  }

  /* Folder */
  .folder { left: 640px; top: 38px; width: 458px; height: 589px; }
  .folder .wordmark { position: absolute; left: 34px; top: 262px; font-size: 21px; gap: 14px; }
  .folder .wordmark .mark { width: 60px; height: 60px; }

  /* Business cards */
  .card-front { left: 43px; top: 657px; width: 204px; height: 120px; }
  .card-front .wordmark { position: absolute; left: 10px; top: 12px; font-size: 5.5px; }
  .card-front .person { position: absolute; left: 10px; top: 38px; font-size: 5px; line-height: 9px; white-space: nowrap; }
  .card-front .person .name { color: var(--brand); }
  .card-front .details { position: absolute; left: 10px; top: 66px; font-size: 4px; line-height: 8px; color: var(--muted); list-style: none; white-space: nowrap; }
  .card-front .corner-mark { position: absolute; right: 14px; bottom: 14px; width: 72px; height: 72px; background: var(--brand); }

  .card-back { left: 43px; top: 787px; width: 204px; height: 105px; }
  .card-back .wordmark { position: absolute; left: 50%; top: 22px; transform: translateX(-50%); font-size: 6px; gap: 6px; }
  .card-back .wordmark .mark { width: 36px; height: 36px; }
  .card-back .web { position: absolute; left: 0; right: 0; bottom: 10px; text-align: center; font-size: 4px; color: var(--muted); letter-spacing: 0.1em; }

  /* Envelopes */
  .envelope-front { left: 267px; top: 667px; width: 441px; height: 207px; }
  .envelope-front .wordmark { position: absolute; left: 16px; top: 16px; font-size: 7.5px; gap: 6px; }
  .envelope-front .wordmark .mark { width: 24px; height: 24px; }

  .envelope-back { left: 739px; top: 672px; width: 431px; height: 207px; overflow: hidden; }
  .envelope-back svg { position: absolute; left: 0; top: 0; }
  .envelope-back .web {
    position: absolute; left: 0; right: 0; top: 24px; text-align: center;
    font-size: 5px; color: var(--flap-text); letter-spacing: 0.35em;
  }
</style>
</head>
<body>

  <section class="sheet letterhead">
    <div class="wordmark"><span class="mark"></span>ZENTH INDUSTRIES</div>
    <ul class="contact">
      <li>Owen Petrie, General Manager</li>
      <li>+6429184306</li>
      <li>sales@zenth.example.nz</li>
      <li>www.zenth.example.nz</li>
    </ul>
    <div class="watermark"></div>
  </section>

  <section class="sheet folder">
    <div class="wordmark"><span class="mark"></span>ZENTH INDUSTRIES</div>
  </section>

  <section class="sheet card-front">
    <div class="wordmark">ZENTH INDUSTRIES</div>
    <div class="person">
      <div class="name">Owen Petrie</div>
      <div class="title">General Manager</div>
    </div>
    <ul class="details">
      <li>+6429184306</li>
      <li>sales@zenth.example.nz</li>
      <li>www.zenth.example.nz</li>
    </ul>
    <div class="corner-mark"></div>
  </section>

  <section class="sheet card-back">
    <div class="wordmark"><span class="mark"></span>ZENTH INDUSTRIES</div>
    <div class="web">www.zenth.example.nz</div>
  </section>

  <section class="sheet envelope-front">
    <div class="wordmark"><span class="mark"></span>ZENTH INDUSTRIES</div>
  </section>

  <section class="sheet envelope-back">
    <svg width="431" height="207" viewBox="0 0 431 207" aria-hidden="true">
      <path d="M0 0 H431 V58 Q215.5 86 0 58 Z" fill="var(--brand)"/>
      <path d="M0 207 L200 110 Q215.5 102 231 110 L431 207" fill="none" stroke="#e3e3e3" stroke-width="1"/>
    </svg>
    <div class="web">www.zenth.example.nz</div>
  </section>

</body>
</html>
```